TK Drafting

Simple Design - Logo is done (from this site). Logo on one side - Back Side an image or outline of a house blue print - My name, phone, email, website url. Prefer the traditional Architectural style of letters -

Target Market(s)

Customers who need a floor plan redesigned for renovations or realtors who want a floor plan for marketing their listings

Industry/Entity Type

Architecture

Contact Information for Business Card

Colby Faust - Name
415-362-8840 - Phone
tkdraftingco@mailpost.example
www.tkdraftingco.example

Font styles to use
Other font styles liked:
• Architecture writing -

Colors
0555a3
3276b5
85acd3

Requirements
Must have
• Logo that is attached. I like an indigo blue color for the background or a royal blue - gray logo OR - white and clean with the logo on one side and the same color gray lettering on the other side
Nice to have
• some sort of image that shows a residential blue print. It may not be possible on this small of a card though.
Should not have
• Nothing cartoonish.

```html
<!DOCTYPE html>
<html lang="en">
<head>
<meta charset="UTF-8">
<title>TK Drafting — Business Card</title>
<link rel="stylesheet" href="https://fonts.googleapis.com/css2?family=Montserrat:wght@300;400;500;700&display=swap">
<style>
  :root {
    --page-bg: #bddff7;
    --royal: #0555a3;
    --mid-blue: #3276b5;
    --light-blue: #85acd3;
    --white: #ffffff;
    --ink: #222222;
    --logo-gray: #b1b1b8;
    --divider: #3f7bbd;
  }
  * { margin: 0; padding: 0; box-sizing: border-box; }
  html, body {
    width: 999px; height: 1200px; overflow: hidden;
    background: var(--page-bg);
    font-family: "Montserrat", sans-serif;
  }
  .canvas { position: relative; width: 999px; height: 1200px; }
  .card {
    position: absolute; left: 64px; width: 845px; height: 483px;
    overflow: hidden;
    box-shadow: 0 14px 30px rgba(40, 90, 140, 0.28);
  }
  .card-front { top: 77px; background: var(--white); }
  .card-back { top: 610px; background: var(--royal); }

  .brand-name {
    position: absolute; color: var(--logo-gray);
    font-weight: 500; letter-spacing: 2px; white-space: nowrap;
    transform: translate(-50%, -50%);
    display: flex; align-items: center; gap: 12px;
  }
  .brand-mark { width: 14px; height: 14px; background: var(--logo-gray); display: inline-block; }
  .card-front .brand-name { left: 717px; top: 106px; font-size: 26px; }
  .card-back .brand-name { left: 169px; top: 241px; font-size: 30px; }

  .holder-name {
    position: absolute; left: 72px; top: 166px;
    font-size: 42px; font-weight: 700; color: var(--royal);
    letter-spacing: 0.3px;
  }
  .holder-title {
    position: absolute; left: 70px; top: 218px;
    font-size: 25px; font-weight: 300; color: var(--ink);
  }

  .contact-band {
    position: absolute; left: 0; top: 274px; width: 100%; height: 209px;
    background: var(--royal);
  }
  .contact-item {
    position: absolute; top: 60px; transform: translateX(-50%);
    display: flex; flex-direction: column; align-items: center; gap: 22px;
    color: var(--white); font-size: 16.5px; font-weight: 400; white-space: nowrap;
  }
  .contact-item svg { width: 26px; height: 26px; }
  .contact-phone { left: 123px; }
  .contact-email { left: 404px; }
  .contact-web { left: 687px; }
  .divider {
    position: absolute; top: 76px; width: 2px; height: 40px;
    background: var(--divider);
  }
  .divider-one { left: 231px; }
  .divider-two { left: 557px; }

  .blueprint-area {
    position: absolute; left: 393px; top: 0; width: 452px; height: 483px;
    background: linear-gradient(120deg, rgba(133,172,211,0.05) 0%, rgba(50,118,181,0.45) 55%, rgba(133,172,211,0.18) 100%);
  }
</style>
</head>
<body>
<main class="canvas">
  <section class="card card-front">
    <div class="brand-name"><span class="brand-mark"></span>TK Drafting</div>
    <h1 class="holder-name">Colby Faust</h1>
    <p class="holder-title">Architect</p>
    <div class="contact-band">
      <div class="contact-item contact-phone">
        <svg viewBox="0 0 24 24" aria-hidden="true"><path fill="#fff" d="M6.6 10.8c1.4 2.8 3.8 5.1 6.6 6.6l2.2-2.2c.3-.3.7-.4 1-.2 1.1.4 2.3.6 3.6.6.6 0 1 .4 1 1V20c0 .6-.4 1-1 1C10.6 21 3 13.4 3 4c0-.6.4-1 1-1h3.5c.6 0 1 .4 1 1 0 1.2.2 2.4.6 3.6.1.3 0 .7-.2 1l-2.3 2.2z"/></svg>
        <span>415-362-8840</span>
      </div>
      <span class="divider divider-one"></span>
      <div class="contact-item contact-email">
        <svg viewBox="0 0 24 24" aria-hidden="true"><circle cx="12" cy="12" r="4" fill="none" stroke="#fff" stroke-width="2.4"/><path d="M16 8v5.5a2.5 2.5 0 0 0 5 0V12a9 9 0 1 0-3.5 7.1" fill="none" stroke="#fff" stroke-width="2.4" stroke-linecap="round"/></svg>
        <span>tkdraftingco@mailpost.example</span>
      </div>
      <span class="divider divider-two"></span>
      <div class="contact-item contact-web">
        <svg viewBox="0 0 24 24" aria-hidden="true"><circle cx="12" cy="12" r="10" fill="#fff"/><path d="M2 12h20M12 2v20M12 2c-3.5 3-3.5 17 0 20M12 2c3.5 3 3.5 17 0 20M4 7h16M4 17h16" fill="none" stroke="#0555a3" stroke-width="1.4"/></svg>
        <span>www.tkdraftingco.example</span>
      </div>
    </div>
  </section>

  <section class="card card-back">
    <div class="blueprint-area" role="img" aria-label="Faint line-drawing blueprint of a modern two-storey house in perspective"></div>
    <div class="brand-name"><span class="brand-mark"></span>TK Drafting</div>
  </section>
</main>
</body>
</html>
```